Delphine Marchetti Photography
Letterhead & Business Card Design
Delphine Marchetti Photography - Photography
Creative Brief
Professional
Delphine Marchetti
Photographer / Owner
517 Bramble Lane Fort McMurray, AB T9K 2P6
delphinemarchettiphotography@pixmail.example
www.delphinemarchettiphotography.example
I think I'd like to include a photo I've taken...thoughts?

```html
<!DOCTYPE html>
<html lang="en">
<head>
<meta charset="utf-8">
<title>Delphine Marchetti Photography – Business Card</title>
<link href="https://fonts.googleapis.com/css2?family=Open+Sans:wght@400;600&display=swap" rel="stylesheet">
<style>
  :root {
    --backdrop: #2e2e2e;
    --card: #ffffff;
    --card-shade: #f4f6f7;
    --accent-blue: #2ba6d3;
    --soft-blue: #d9eef6;
    --brand-brown: #7b5a46;
    --body-text: #4e4e4e;
  }
  * { margin: 0; padding: 0; box-sizing: border-box; }
  html, body {
    width: 1200px; height: 780px; overflow: hidden;
    background: var(--backdrop);
    font-family: "Open Sans", Arial, sans-serif;
  }
  .canvas { position: relative; width: 1200px; height: 780px; }
  .business-card {
    position: absolute; left: 150px; top: 125px;
    width: 900px; height: 530px;
    background: linear-gradient(180deg, var(--card) 0%, var(--card-shade) 100%);
    border-radius: 26px; overflow: hidden;
  }
  .edge-tab {
    position: absolute; left: 0; top: 340px;
    width: 14px; height: 120px; background: var(--accent-blue);
  }
  .faint-emblem {
    position: absolute; left: 560px; top: 20px;
    width: 330px; height: 330px; border-radius: 50%;
    background: radial-gradient(circle, #f3f9fc 0%, var(--soft-blue) 75%, #eaf5fa 100%);
    opacity: 0.7;
  }
  .brand {
    position: absolute; left: 60px; top: 70px;
    display: flex; align-items: center; gap: 22px;
  }
  .brand-dot {
    width: 118px; height: 118px; border-radius: 50%;
    background: var(--accent-blue);
  }
  .brand-name {
    font-size: 40px; font-weight: 400; color: var(--brand-brown);
    line-height: 1.1; letter-spacing: 0.5px;
  }
  .person {
    position: absolute; left: 630px; top: 222px; text-align: center; width: 200px;
  }
  .person-name { font-size: 22px; font-weight: 600; color: var(--accent-blue); }
  .person-role { font-size: 17px; color: var(--brand-brown); margin-top: 4px; }
  .address {
    position: absolute; left: 60px; top: 255px;
    font-size: 17px; line-height: 1.4; color: var(--body-text);
  }
  .contact-list {
    position: absolute; left: 60px; top: 330px; list-style: none;
    font-size: 17px; color: var(--body-text);
  }
  .contact-list li { display: flex; align-items: center; gap: 12px; height: 30px; }
  .contact-list svg { width: 18px; height: 18px; fill: var(--accent-blue); flex: none; }
</style>
</head>
<body>
<div class="canvas">
  <div class="business-card">
    <div class="faint-emblem" role="img" aria-label="Faint decorative circular pattern"></div>
    <div class="edge-tab"></div>

    <div class="brand">
      <div class="brand-dot"></div>
      <div class="brand-name">Delphine Marchetti<br>Photography</div>
    </div>

    <div class="person">
      <div class="person-name">Delphine Marchetti</div>
      <div class="person-role">Photographer / Owner</div>
    </div>

    <address class="address" style="font-style:normal">
      517 Bramble Lane<br>
      Fort McMurray, AB T9K 2P6
    </address>

    <ul class="contact-list">
      <li>
        <svg viewBox="0 0 24 24" aria-hidden="true"><path d="M6.6 10.8a15 15 0 0 0 6.6 6.6l2.2-2.2c.3-.3.7-.4 1-.2 1.1.4 2.3.6 3.6.6.6 0 1 .4 1 1V20c0 .6-.4 1-1 1A17 17 0 0 1 3 4c0-.6.4-1 1-1h3.5c.6 0 1 .4 1 1 0 1.3.2 2.5.6 3.6.1.3 0 .7-.2 1z"/></svg>
        780.555.0142
      </li>
      <li>
        <svg viewBox="0 0 24 24" aria-hidden="true"><path d="M7 2h10a2 2 0 0 1 2 2v16a2 2 0 0 1-2 2H7a2 2 0 0 1-2-2V4a2 2 0 0 1 2-2zm0 3v12h10V5zm5 13.5a1 1 0 1 0 0 2 1 1 0 0 0 0-2z"/></svg>
        780.555.0187
      </li>
      <li>
        <svg viewBox="0 0 24 24" aria-hidden="true"><path d="M12 2a10 10 0 1 0 5 18.7l-1-1.7A8 8 0 1 1 20 12v1.2a1.8 1.8 0 0 1-3.6 0V12a4.4 4.4 0 1 0-1.3 3.1 3.8 3.8 0 0 0 6.9-1.9V12A10 10 0 0 0 12 2zm0 12.4a2.4 2.4 0 1 1 0-4.8 2.4 2.4 0 0 1 0 4.8z"/></svg>
        delphinemarchettiphotography@pixmail.example
      </li>
      <li>
        <svg viewBox="0 0 24 24" aria-hidden="true"><path d="M12 2a10 10 0 1 0 0 20 10 10 0 0 0 0-20zm6.9 6h-2.9a15 15 0 0 0-1.3-3.6A8 8 0 0 1 18.9 8zM12 4a13 13 0 0 1 1.9 4h-3.8A13 13 0 0 1 12 4zM4.3 14a8 8 0 0 1 0-4h3.4a16 16 0 0 0 0 4zm.8 2h2.9a15 15 0 0 0 1.3 3.6A8 8 0 0 1 5.1 16zM8 8H5.1a8 8 0 0 1 4.2-3.6A15 15 0 0 0 8 8zm4 12a13 13 0 0 1-1.9-4h3.8A13 13 0 0 1 12 20zm2.3-6H9.7a14 14 0 0 1 0-4h4.6a14 14 0 0 1 0 4zm.4 5.6A15 15 0 0 0 16 16h2.9a8 8 0 0 1-4.2 3.6zm1.6-5.6a16 16 0 0 0 0-4h3.4a8 8 0 0 1 0 4z"/></svg>
        www.delphinemarchettiphotography.example
      </li>
    </ul>
  </div>
</div>
</body>
</html>
```